Meridel Hair Studio Needs a new appointment business card

We need a new appointment card for our hair salon.

I Dont want bright out there colours.
I would like it to be neat, clean, easy to read. White, Black, with a hint of colour if needed.

We need
-Logo
-Phone number 47208613
-Mobile Number: 0417306852
Address: Shop 3/214 Calder Road, The Elmgates, Tarrowby 4862

BACK SIDE OF CARD
- Appointment Time & Date (White background so we are able to write on it)
(If you are unable to make your appointment please contact us ASAP 47208613)

I also would like the chatterly and Pictorama logo(Find us on Chatterly)(find us on Pictorama)

Target Market(s)

appointment card simple to read. all information for their next appoint For all our clients male and female

Industry/Entity Type

Hairdresser

Contact Information for Business Card

-Logo
-Phone number 47208613

BACK SIDE OF CARD

Font styles to use
Serif
Sans Serif
Script

Requirements
Must have
• White Back ground on backside with appointment deatils so we are able to write information (like appointment time and date)
Nice to have
• Find us on Chatterly
and
pictorama - meridel_hairstudio
Should not have
• BRIGHT COLOURS

```html
<!DOCTYPE html>
<html lang="en">
<head>
<meta charset="utf-8">
<title>Meridel Hair Studio – Appointment Card</title>
<link rel="stylesheet" href="https://fonts.googleapis.com/css2?family=Poppins:wght@300;400;500&display=swap">
<style>
  :root {
    --page: #e4e3e0;
    --card-dark: #252322;
    --card-light: #eeedea;
    --ink-light: #f2f0ec;
    --ink-grey: #7a7774;
    --accent: #d4b79a;
  }
  * { box-sizing: border-box; margin: 0; padding: 0; }
  html, body { width: 1200px; height: 800px; overflow: hidden; }
  body {
    background: var(--page);
    font-family: "Poppins", sans-serif;
    display: flex;
    align-items: center;
    justify-content: center;
    gap: 44px;
  }
  .card {
    position: relative;
    width: 540px;
    height: 310px;
    border-radius: 3px;
    overflow: hidden;
    box-shadow: 0 10px 28px rgba(0,0,0,0.12);
  }
  .card--front { background: var(--card-dark); color: var(--ink-light); text-align: center; }
  .card--back { background: var(--card-light); color: var(--ink-grey); text-align: center; }

  .brand { position: absolute; top: 70px; left: 0; right: 0; }
  .brand__name {
    font-weight: 400; font-size: 34px; letter-spacing: 2px; text-transform: uppercase; line-height: 1;
  }
  .brand__sub {
    margin-top: 8px; font-weight: 400; font-size: 12px; letter-spacing: 5px; text-transform: uppercase;
  }
  .divider { width: 20px; height: 3px; background: var(--accent); margin: 18px auto 16px; }
  .contact { font-size: 12.5px; font-weight: 400; line-height: 1.75; letter-spacing: 0.3px; }
  .contact span + span { margin-left: 8px; }

  .tool-strip { position: absolute; left: 0; right: 0; bottom: 14px; height: 30px; }
  .card--front .tool-strip {
    background: linear-gradient(90deg, rgba(212,183,154,0.35), rgba(212,183,154,0.5), rgba(212,183,154,0.35));
  }
  .card--back .tool-strip {
    background: linear-gradient(90deg, rgba(212,183,154,0.22), rgba(212,183,154,0.35), rgba(212,183,154,0.22));
  }

  .appointment {
    position: absolute; top: 28px; left: 60px; right: 60px; height: 146px;
    border: 1px solid var(--accent);
    padding: 22px 34px 0;
    text-align: left;
  }
  .appointment__title {
    font-size: 17px; font-weight: 400; letter-spacing: 1.5px; text-align: center; margin-bottom: 20px;
  }
  .field { display: flex; align-items: flex-end; font-size: 14px; letter-spacing: 0.5px; margin-bottom: 20px; }
  .field__label { width: 60px; }
  .field__line { flex: 1; border-bottom: 1px solid var(--ink-grey); height: 14px; }
  .field__sep { padding: 0 6px; line-height: 1; }

  .notice {
    position: absolute; top: 184px; left: 0; right: 0;
    font-size: 11.5px; line-height: 1.45; letter-spacing: 0.4px;
  }
  .social {
    position: absolute; top: 224px; left: 0; right: 0; font-size: 11.5px; letter-spacing: 0.4px; line-height: 1.45;
  }
  .social__networks { color: var(--accent); margin-left: 4px; }
  .social__handle { font-size: 10.5px; margin-top: 1px; }
</style>
</head>
<body>

  <section class="card card--front" aria-label="Card front">
    <div class="brand">
      <div class="brand__name">Meridel</div>
      <div class="brand__sub">Hair-Studio</div>
      <div class="divider"></div>
      <p class="contact"><span>Tel. 47208613</span><span>Mobile. 0417306852</span><br>
        Address. Shop 3/214 Calder Road, The Elmgates, Tarrowby 4862</p>
    </div>
    <div class="tool-strip" role="img" aria-label="Row of line-drawn hair tools: scissors, combs, brushes, hair dryers and mirrors"></div>
  </section>

  <section class="card card--back" aria-label="Card back">
    <div class="appointment">
      <h2 class="appointment__title">Your Next Appointment:</h2>
      <div class="field">
        <span class="field__label">Date:</span>
        <span class="field__line"></span><span class="field__sep">/</span>
        <span class="field__line"></span><span class="field__sep">/</span>
        <span class="field__line"></span>
      </div>
      <div class="field">
        <span class="field__label">Time:</span>
        <span class="field__line"></span>
      </div>
    </div>
    <p class="notice">If you are unable to make your appointment<br>please contact us ASAP 47208613</p>
    <div class="social">
      <p>Find us on <span class="social__networks">Chatterly · Pictorama</span></p>
      <p class="social__handle">meridel_hairstudio</p>
    </div>
    <div class="tool-strip" role="img" aria-label="Row of line-drawn hair tools: scissors, combs, brushes, hair dryers and mirrors"></div>
  </section>

</body>
</html>
```